HiItsJonBrell.com needs a modern, eye-catching business card design

My name is Jon Brell and I own a video training (software development industry) website. I need a business card design that is eye catching for when I travel to conferences or do seminars. I would prefer something simple but bold. Something along the lines of this: https://pixvaultstatic.example/gallery_img/530172/44018/44018_9917302_530172_image.jpg

Note that I do not have a specific logo, but I do have an caricature I use on my site of myself. I've not attached it because I'm not really a fan of having it on my business cards. I would prefer lettering instead of an image. You can go to my website (https://hiitsjonbrell.com) for inspiration.

I want to add the following information on my card (the order of these, their size, and their casing is up to you):

Jon Brell
jon@HiItsJonBrell.com
@HiItsJonBrell
HiItsJonBrell.com
vidsharehub.example/HiItsJonBrell

I would also like to have somewhere on the card a small ad that says "Get a free course at https://HiItsJonBrell.com/FreeCourse". Feel free to play with that wording or layout if you need. I would prefer this text to be at the bottom of the card and subtle. Some small eye-catching thing might be ok but nothing huge or garish.

I plan on printing this card at pressquill.example (https://www.pressquill.example/us/design-guidelines/business-cards.html). I would like it to be the standard size (3.66" x 2.16"). I would prefer rounded corners and horizontal orientation. This is a two-side design. I would prefer the side with all of the information be primarily white but I like color text (again, flexible on that). On the front side, I like simple. Maybe just HiItsJonBrell.com (casing on that is up to you - whatever looks and reads the best - that goes for all of the casing). As for font choices, I prefer a modern, clean font. For example, Open Sans Light can be a nice option.

Website Info (might be helpful for the card):
Color Palette

Darkest blue - #263246
Alternate blue - #2F4E6A
Light blue - #2A98C3
Orange - #FF6201
White - #FFFFFF

Font for Jon Brell Logo

Jellyka Estryas Handwriting
http://www.typecrate.example/jellyka_estryas_handwriting.font

Fonts for Site Content and VidShare Thumbnails

Lovelo (bold title font)
http://www.glyphmill.example/lovelo-font/

Open Sans (body font)
http://www.letterbarn.example/fonts/open-sans

Industry/Entity Type

Software Development

Contact Information for Business Card

Jon Brell
jon@HiItsJonBrell.com
@HiItsJonBrell
HiItsJonBrell.com
vidsharehub.example/HiItsJonBrell

Get a free course at https://HiItsJonBrell.com/FreeCourse

Colors

Designer to choose colors to be used in the design.

Requirements
Nice to have
• Modern color - maybe primarily a color on the front and then that color as an accent on the back.
Should not have
• Lots of colors - I LOVE color but do not want a rainbow of colors on the card.

```html
<!DOCTYPE html>
<html lang="en">
<head>
<meta charset="utf-8">
<title>Jon Brell – Business Card</title>
<link rel="stylesheet" href="https://fonts.googleapis.com/css2?family=Open+Sans:wght@300;400;700&family=Josefin+Sans:wght@700&display=swap">
<style>
  :root {
    --navy: #263246;
    --alt-blue: #2F4E6A;
    --light-blue: #2A98C3;
    --white: #FFFFFF;
    --backdrop: #E8E6E2;
  }
  * { margin: 0; padding: 0; box-sizing: border-box; }
  html, body { width: 1200px; height: 1000px; overflow: hidden; }
  body { background: var(--backdrop); position: relative; font-family: "Open Sans", sans-serif; }

  .card { position: absolute; overflow: hidden; box-shadow: 0 4px 14px rgba(0,0,0,.25); }

  /* Information side */
  .card--info { left: 222px; top: 63px; width: 755px; height: 432px; background: var(--white); }
  .card__name-panel {
    position: absolute; left: 0; top: 0; width: 351px; height: 377px;
    display: flex; align-items: center; justify-content: center;
    box-shadow: 4px 0 10px rgba(0,0,0,.18); background: var(--white); z-index: 1;
  }
  .name-mark { font-weight: 300; color: var(--navy); font-size: 56px; letter-spacing: -0.5px; }

  .contact-list { position: absolute; left: 351px; top: 0; list-style: none; }
  .contact-item { position: absolute; left: 0; display: flex; align-items: center; white-space: nowrap; }
  .contact-item:nth-child(1) { top: 56px; }
  .contact-item:nth-child(2) { top: 141px; }
  .contact-item:nth-child(3) { top: 218px; }
  .contact-item:nth-child(4) { top: 293px; }
  .contact-icon {
    width: 48px; height: 48px; background: var(--navy);
    display: flex; align-items: center; justify-content: center;
    box-shadow: 2px 3px 5px rgba(0,0,0,.3); flex: none;
  }
  .contact-text { margin-left: 18px; font-size: 24px; color: var(--alt-blue); }
  .contact-text--long { font-size: 19px; }

  .promo-band {
    position: absolute; left: 0; bottom: 0; width: 100%; height: 55px;
    background: var(--light-blue); display: flex; align-items: center; justify-content: center;
    font-family: "Josefin Sans", sans-serif; font-weight: 700; font-size: 19px;
    text-transform: uppercase; letter-spacing: .3px; padding-top: 3px; z-index: 2;
  }
  .promo-band__lead { color: var(--navy); margin-right: 7px; }
  .promo-band__url { color: var(--white); }

  /* Front side */
  .card--front {
    left: 224px; top: 523px; width: 751px; height: 429px; background: var(--navy);
  }
  .front-name {
    position: absolute; left: 0; width: 100%; top: 92px; text-align: center;
    font-weight: 300; font-size: 104px; color: var(--white); letter-spacing: -1px;
  }
  .front-url {
    position: absolute; left: 0; width: 100%; top: 300px; text-align: center;
    font-weight: 700; font-size: 29px; color: var(--light-blue);
  }
</style>
</head>
<body>

<section class="card card--info" aria-label="Business card, information side">
  <div class="card__name-panel">
    <span class="name-mark">Jon Brell</span>
  </div>

  <ul class="contact-list">
    <li class="contact-item">
      <span class="contact-icon">
        <svg width="36" height="36" viewBox="0 0 36 36" fill="none" stroke="#2A98C3" stroke-width="2.2">
          <circle cx="18" cy="18" r="15"/>
          <ellipse cx="18" cy="18" rx="7" ry="15"/>
          <line x1="18" y1="3" x2="18" y2="33"/>
          <line x1="3" y1="18" x2="33" y2="18"/>
          <line x1="6" y1="10" x2="30" y2="10"/>
          <line x1="6" y1="26" x2="30" y2="26"/>
        </svg>
      </span>
      <span class="contact-text">HiItsJonBrell.com</span>
    </li>
    <li class="contact-item">
      <span class="contact-icon">
        <svg width="38" height="28" viewBox="0 0 38 28">
          <rect x="1" y="1" width="36" height="26" fill="#2A98C3"/>
          <polyline points="1,1 19,16 37,1" fill="none" stroke="#263246" stroke-width="2"/>
          <line x1="1" y1="27" x2="14" y2="12" stroke="#263246" stroke-width="2"/>
          <line x1="37" y1="27" x2="24" y2="12" stroke="#263246" stroke-width="2"/>
        </svg>
      </span>
      <span class="contact-text">@HiItsJonBrell</span>
    </li>
    <li class="contact-item">
      <span class="contact-icon">
        <svg width="38" height="28" viewBox="0 0 38 28">
          <rect x="1" y="1" width="36" height="26" fill="#2A98C3"/>
          <polyline points="1,1 19,16 37,1" fill="none" stroke="#263246" stroke-width="2"/>
          <line x1="1" y1="27" x2="14" y2="12" stroke="#263246" stroke-width="2"/>
          <line x1="37" y1="27" x2="24" y2="12" stroke="#263246" stroke-width="2"/>
        </svg>
      </span>
      <span class="contact-text">jon@HiItsJonBrell.com</span>
    </li>
    <li class="contact-item">
      <span class="contact-icon" aria-hidden="true"></span>
      <span class="contact-text contact-text--long">vidsharehub.example/HiItsJonBrell</span>
    </li>
  </ul>

  <div class="promo-band">
    <span class="promo-band__lead">Get a free course at</span>
    <span class="promo-band__url">https://HiItsJonBrell.com/FreeCourse</span>
  </div>
</section>

<section class="card card--front" aria-label="Business card, front side">
  <p class="front-name">Jon Brell</p>
  <p class="front-url">www.HiItsJonBrell.com</p>
</section>

</body>
</html>
```